Kinsmen Crest Beard Oil Label for 1oz dropper bottle

Create a label for a 1oz beard oil dropper bottle. The label is 1.5 inches tall and 2.75 inches wide. Our logo is listed in the brief so please use it but it doesnt have to be that prominent. BEARD OIL is the most important verbiage. We like elements of all the attached images but we want our own look and feel.

Target Market(s)

Men with beards

Requirements
Must have
• Kinsmen Crest Logo, BEARD OIL, Flavor (Tobacco Vanilla)

Ingredients
Fractionated Coconut Oil (MCT)
Golden Jojoba Oil
Hemp Seed Oil
Tea Tree Essential Oil
Orange Bitter Essential Oil
Peppermint Supreme Essential Oil
Tallow Aromas
DYE FREE

Directions:
Directions: apply 3-6 drops into your hand...rub oil into hands and apply directly onto beard. For best results massage into skin under beard area and work oil out towards beard. Discontinue use if skin becomes irritated.

100% MADE IN THE USA (American Flag 1 color)
Veteran Owned Co.
Nice to have
• Labels can change color with each flavor or a ring can change color to show flavor.

```html
<!DOCTYPE html>
<html lang="en">
<head>
<meta charset="utf-8">
<title>Kinsmen Crest Beard Oil – Tobacco Vanilla Label</title>
<link rel="stylesheet" href="https://fonts.googleapis.com/css2?family=Andika:wght@400;700&family=Rye&family=Pinyon+Script&family=Cutive+Mono&display=swap">
<style>
  :root {
    --page: #ffffff;
    --parchment-light: #f7eed6;
    --parchment-dark: #e6d3aa;
    --ink: #2b231c;
    --brown: #3e2417;
    --gold: #8d6a2c;
    --mint: #5ef0a8;
    --rule: #2b231c;
    --beard-dark: #3a3a3a;
    --beard-light: #b9b9b9;
  }
  * { box-sizing: border-box; margin: 0; padding: 0; }
  html, body { width: 1200px; height: 533px; overflow: hidden; background: var(--page); }
  .canvas { position: relative; width: 1200px; height: 533px; }

  .label {
    position: absolute; left: 142px; top: 16px; width: 916px; height: 500px;
    background: radial-gradient(ellipse at 55% 45%, var(--parchment-light) 0%, #f1e4c3 55%, var(--parchment-dark) 100%);
    font-family: "Andika", sans-serif; color: var(--ink);
    overflow: hidden;
  }

  /* left panel */
  .claims { position: absolute; left: 30px; top: 46px; width: 182px; text-align: center; font-size: 13.5px; line-height: 20.5px; letter-spacing: 0.3px; }
  .claims .rule { height: 2px; background: var(--rule); margin: 14px 0 12px; }
  .flag { display: block; margin: 10px auto 0; }
  .veteran { position: absolute; left: 30px; top: 423px; width: 182px; text-align: center; color: var(--mint); font-size: 13.5px; letter-spacing: 0.3px; }

  .tagline {
    position: absolute; left: 204px; top: 42px; width: 30px; height: 430px;
    writing-mode: vertical-rl; text-align: center;
    font-family: "Cutive Mono", monospace; font-size: 21px; letter-spacing: 2.5px; color: var(--mint);
  }

  /* centre panel */
  .beard-art {
    position: absolute; left: 392px; top: 10px; width: 142px; height: 140px;
    background: linear-gradient(180deg, var(--beard-light), var(--beard-dark));
    border-radius: 10px 10px 60px 60px;
  }
  .brand {
    position: absolute; left: 262px; top: 178px; width: 400px; text-align: center;
    font-family: "Andika", sans-serif; font-weight: 700; font-size: 56px; line-height: 62px; color: var(--mint);
  }
  .brand .mark { display: inline-block; width: 22px; height: 22px; border-radius: 50%; background: var(--mint); margin-top: 12px; }
  .product {
    position: absolute; left: 262px; top: 306px; width: 400px; text-align: center;
    font-family: "Rye", serif; font-size: 60px; line-height: 68px; color: var(--brown); letter-spacing: 1px;
  }
  .flavor {
    position: absolute; left: 262px; top: 388px; width: 400px; text-align: center;
    font-family: "Pinyon Script", cursive; font-size: 52px; line-height: 70px; color: var(--gold);
  }
  .volume { position: absolute; left: 557px; top: 456px; font-size: 13px; color: var(--mint); letter-spacing: 0.3px; }

  /* right panel */
  .info { position: absolute; left: 688px; top: 28px; width: 188px; text-align: center; font-size: 13.5px; line-height: 20.5px; letter-spacing: 0.3px; }
  .info h2 { font-size: 19px; font-weight: 700; color: var(--gold); line-height: 26px; letter-spacing: 0.5px; }
  .info .rule { height: 2px; background: var(--rule); margin: 6px 6px 8px; }
  .info .note { margin-top: 16px; }
</style>
</head>
<body>
<main class="canvas">
  <section class="label" aria-label="Kinsmen Crest Beard Oil label, Tobacco Vanilla">

    <div class="claims">
      <p>Original BEARD OIL<br>Posses a<br>MASCULINE SCENT<br>and a light<br>Character as it<br>gently Moisturizes<br>Your face.</p>
      <div class="rule"></div>
      <p>Use 2 - 3 times<br>per week</p>
      <div class="rule"></div>
      <p>Original<br>100 % made in USA</p>
      <svg class="flag" width="118" height="62" viewBox="0 0 118 62" role="img" aria-label="American flag, one colour">
        <g fill="var(--ink)">
          <rect x="0" y="0" width="118" height="4.8"/>
          <rect x="0" y="9.5" width="118" height="4.8"/>
          <rect x="0" y="19" width="118" height="4.8"/>
          <rect x="0" y="28.5" width="118" height="4.8"/>
          <rect x="0" y="38" width="118" height="4.8"/>
          <rect x="0" y="47.5" width="118" height="4.8"/>
          <rect x="0" y="57" width="118" height="4.8"/>
          <rect x="0" y="0" width="50" height="33.3"/>
        </g>
        <g fill="var(--parchment-light)">
          <circle cx="6" cy="5" r="1.3"/><circle cx="14" cy="5" r="1.3"/><circle cx="22" cy="5" r="1.3"/><circle cx="30" cy="5" r="1.3"/><circle cx="38" cy="5" r="1.3"/><circle cx="46" cy="5" r="1.3"/>
          <circle cx="10" cy="11" r="1.3"/><circle cx="18" cy="11" r="1.3"/><circle cx="26" cy="11" r="1.3"/><circle cx="34" cy="11" r="1.3"/><circle cx="42" cy="11" r="1.3"/>
          <circle cx="6" cy="17" r="1.3"/><circle cx="14" cy="17" r="1.3"/><circle cx="22" cy="17" r="1.3"/><circle cx="30" cy="17" r="1.3"/><circle cx="38" cy="17" r="1.3"/><circle cx="46" cy="17" r="1.3"/>
          <circle cx="10" cy="23" r="1.3"/><circle cx="18" cy="23" r="1.3"/><circle cx="26" cy="23" r="1.3"/><circle cx="34" cy="23" r="1.3"/><circle cx="42" cy="23" r="1.3"/>
          <circle cx="6" cy="29" r="1.3"/><circle cx="14" cy="29" r="1.3"/><circle cx="22" cy="29" r="1.3"/><circle cx="30" cy="29" r="1.3"/><circle cx="38" cy="29" r="1.3"/><circle cx="46" cy="29" r="1.3"/>
        </g>
      </svg>
    </div>
    <p class="veteran">Veteran Owned Co.</p>

    <p class="tagline">QUALITY &amp; CRAFTSMANSHIP</p>

    <div class="beard-art" role="img" aria-label="Illustration of a full drawn beard and moustache in grey linework"></div>
    <h1 class="brand">Kinsmen <span class="mark" aria-hidden="true"></span><br>Crest</h1>
    <p class="product">BEARD OIL</p>
    <p class="flavor">Tobacco Vanilla</p>
    <p class="volume">30 ML / 1FL.OZ</p>

    <div class="info">
      <h2>Ingredients</h2>
      <p>Fractionated Coconut Oil (MCT), Golden Jojoba Oil, Hemp Seed Oil, Tea Tree Essential Oil, Orange Bitter Essential Oil, Peppermint Supreme Essential Oil, Tallow Aromas<br>DYE FREE</p>
      <div class="rule"></div>
      <h2>Directions:</h2>
      <p>Apply 3-6 drops into your hand…rub oil into hands and apply directly onto beard. For best results massage into skin under beard area and work oil out towards beard.</p>
      <div class="rule"></div>
      <p class="note">***Discontinue use if skin becomes irritated.</p>
    </div>

  </section>
</main>
</body>
</html>
```